Layout für Werbefahnen gesucht
Zielgruppe
Unsere Frühstückpension befindet sich in Jois am Neusiedlersee mit direktem Leithabergblick. Wir haben auch ein Weingut was unsere Gäste sehr schätzen.
Unsere Zielgruppe sind Urlaubsgäste mit höheren Ansprüchen sowie Weinbegeistere , Naturliebhaber, Radfahrer und Seeliebhaber (Neusiedlersee) unser Haus wurde mit sehr hochwertigen Materialien ausgestattet.
Aufgabenstellung
3 STK Werbefahnen ( Fahnenmast stehen schon siehe Beilage Bild) Maße: Format 1000x4000 mm
Unser Logo sollte auf den Fahnen vorhanden sein, man soll erkennen - dass man hier Urlaub verbringen kann und Wein verkosten (genießen) oder auch kaufen kann.
Gerne mit netten kurzen Sprüchen oder Wortspielen (Urlaub mit Leithabergblick oder so?.
Naturverbunden mit liebe zum Wein, die Farben sollten unserem Logo angepasst werden eher naturverbunden braun oder grün, 1 Fahne sollte nur für den Wein gestaltet werden und die anderen beiden für unser Gästehaus.

```html
<!DOCTYPE html>
<html lang="de">
<head>
<meta charset="utf-8">
<title>Gut Haldenrain – Werbefahnen</title>
<link href="https://fonts.googleapis.com/css2?family=Libre+Caslon+Text:wght@400;700&display=swap" rel="stylesheet">
<style>
  :root {
    --page-bg: #ececec;
    --flag-bg: #ffffff;
    --brand-brown: #6b3a1a;
    --word-tan: #bf9a7f;
    --sky-top: #ffffff;
    --sky-mid: #e4eef5;
    --sky-low: #cfe0ec;
    --lake-deep: #1d4a78;
    --field-green: #8d9a3a;
    --field-yellow: #b9b64a;
    --vine-dark: #2f4a2a;
    --vine-mid: #5d7a45;
    --product-dark: #1c1d3e;
    --product-mid: #2b2d55;
  }
  * { margin: 0; padding: 0; box-sizing: border-box; }
  html, body { width: 1000px; height: 1200px; overflow: hidden; }
  body {
    background: var(--page-bg);
    font-family: "Libre Caslon Text", Georgia, serif;
    position: relative;
  }
  .flag {
    position: absolute;
    top: 65px;
    width: 267px;
    height: 1072px;
    background: var(--flag-bg);
    overflow: hidden;
  }
  .flag--wellbeing { left: 59px; }
  .flag--wine { left: 366px; }
  .flag--holiday { left: 670px; }

  .brand {
    position: absolute;
    top: 70px;
    left: 0;
    width: 100%;
    text-align: center;
    color: var(--brand-brown);
    z-index: 3;
  }
  .brand__name {
    font-weight: 700;
    font-size: 22px;
    line-height: 1.1;
    letter-spacing: 0;
    white-space: nowrap;
  }
  .brand__tagline {
    margin-top: 10px;
    font-size: 14px;
    font-weight: 400;
    letter-spacing: 0.6px;
    white-space: nowrap;
  }

  .photo { position: absolute; left: 0; width: 100%; z-index: 1; }

  .photo--house {
    top: 184px; height: 305px;
    background: linear-gradient(180deg, rgba(225,232,245,0) 0%, #dfe6f0 18%, #e9ecee 45%, #aebf8a 70%, rgba(190,205,160,0) 100%);
  }
  .photo--harbour {
    top: 758px; height: 314px;
    background: linear-gradient(180deg, rgba(255,255,255,0) 0%, #d4dee6 20%, #9aa98c 32%, #b6c8d8 45%, #6c90b4 70%, var(--lake-deep) 100%);
  }
  .photo--sky-field {
    top: 205px; height: 867px;
    background: linear-gradient(180deg, var(--sky-top) 0%, var(--sky-mid) 35%, var(--sky-low) 60%, #dde6df 68%, #5f7a45 74%, var(--field-green) 82%, var(--field-yellow) 100%);
  }
  .photo--product {
    left: 91px; width: 86px;
    top: 669px; height: 328px;
    background: linear-gradient(180deg, var(--product-mid) 0%, var(--product-dark) 100%);
    z-index: 2;
  }
  .photo--sky-vineyard {
    top: 205px; height: 867px;
    background: linear-gradient(180deg, var(--sky-top) 0%, var(--sky-mid) 40%, var(--sky-low) 70%, #c7d0cf 74%, #9ea87e 78%, var(--vine-mid) 84%, var(--vine-dark) 100%);
  }

  .claim {
    position: absolute;
    writing-mode: vertical-rl;
    color: var(--word-tan);
    font-weight: 700;
    line-height: 1;
    z-index: 2;
    white-space: nowrap;
  }
  .claim--wellbeing {
    top: 346px; left: 102px;
    font-size: 64px;
    letter-spacing: -4px;
  }
  .claim--wine {
    top: 175px; left: 106px;
    font-size: 62px;
    letter-spacing: -3px;
  }
  .claim--holiday {
    top: 212px; left: 98px;
    font-size: 86px;
    letter-spacing: -5px;
  }
</style>
</head>
<body>
  <section class="flag flag--wellbeing">
    <div class="brand">
      <div class="brand__name">GUT HALDENRAIN</div>
      <div class="brand__tagline">Schlafen am Neusiedler See</div>
    </div>
    <div class="photo photo--house" role="img" aria-label="Gästehaus mit Terrasse, Pool und Liegewiese"></div>
    <div class="photo photo--harbour" role="img" aria-label="Segelhafen am See mit Holzpfählen im ruhigen Wasser"></div>
    <h2 class="claim claim--wellbeing">WOHLFÜHLEN</h2>
  </section>

  <section class="flag flag--wine">
    <div class="brand">
      <div class="brand__name">GUT HALDENRAIN</div>
      <div class="brand__tagline">Schlafen am Neusiedler See</div>
    </div>
    <div class="photo photo--sky-field" role="img" aria-label="Himmel über sanften Hügeln, Weingärten und grünem Feld"></div>
    <div class="photo photo--product" role="img" aria-label="Produktfoto: Rotweinflasche des Hauses"></div>
    <h2 class="claim claim--wine">WEINGENUSS</h2>
  </section>

  <section class="flag flag--holiday">
    <div class="brand">
      <div class="brand__name">GUT HALDENRAIN</div>
      <div class="brand__tagline">Schlafen am Neusiedler See</div>
    </div>
    <div class="photo photo--sky-vineyard" role="img" aria-label="Junger Weingarten mit Blick auf den See im Morgennebel"></div>
    <h2 class="claim claim--holiday">URLAUB</h2>
  </section>
</body>
</html>
```